Business Card Design Project

Need a business card with logo that is attached.
Company name: Moberly Swift Solutions, LLC
My name: Lucia Pembrook
Title: President
Phone number: 703-482-1947
Email: lpembrook@moberlyswiftsolutions.example
web site: www.moberlyswiftsolutions.example

Industry/Entity Type

Business

```html
<!DOCTYPE html>
<html lang="en">
<head>
<meta charset="utf-8">
<title>Moberly Swift Solutions — Business Card</title>
<link href="https://fonts.googleapis.com/css2?family=Anton&family=Questrial&display=swap" rel="stylesheet">
<style>
  :root {
    --page-bg: #e9e7e4;
    --card-black: #050505;
    --card-white: #ffffff;
    --accent-blue: #1d7fd6;
    --accent-indigo: #3b3fa8;
    --brand-teal: #1f8f86;
    --brand-blue: #2a5fa8;
    --ink: #111111;
  }
  html, body {
    margin: 0;
    width: 1200px;
    height: 1200px;
    overflow: hidden;
    background: var(--page-bg);
  }
  .stage {
    width: 1200px;
    height: 1200px;
    display: flex;
    align-items: center;
    justify-content: center;
  }
  .card {
    position: relative;
    width: 560px;
    height: 980px;
    background: var(--card-black);
    box-shadow: 0 10px 30px rgba(0,0,0,0.18);
    overflow: hidden;
  }
  .card-shape {
    position: absolute;
    inset: 0;
  }
  .brand {
    position: absolute;
    top: 190px;
    left: 0;
    right: 0;
    display: flex;
    align-items: center;
    justify-content: center;
    gap: 18px;
  }
  .brand-dot {
    width: 64px;
    height: 64px;
    border-radius: 50%;
    background: var(--brand-teal);
    flex: none;
  }
  .brand-name {
    font-family: "Questrial", sans-serif;
    font-size: 25px;
    line-height: 1.2;
    letter-spacing: 1px;
    text-transform: uppercase;
    color: var(--brand-blue);
    margin: 0;
  }
  .person {
    position: absolute;
    top: 400px;
    left: 0;
    right: 0;
    text-align: center;
    color: var(--ink);
  }
  .person-name {
    font-family: "Anton", sans-serif;
    font-size: 40px;
    margin: 0;
    line-height: 1.1;
  }
  .person-title {
    font-family: "Anton", sans-serif;
    font-size: 20px;
    font-weight: 400;
    margin: 6px 0 0;
  }
  .contact {
    position: absolute;
    top: 610px;
    left: 30px;
    right: 30px;
    text-align: center;
    font-family: "Questrial", sans-serif;
    color: var(--ink);
  }
  .contact-phone {
    font-size: 32px;
    margin: 0 0 10px;
  }
  .contact-line {
    font-size: 21px;
    margin: 0 0 4px;
  }
</style>
</head>
<body>
  <main class="stage">
    <article class="card">
      <svg class="card-shape" width="560" height="980" viewBox="0 0 560 980" aria-hidden="true">
        <path d="M0 170 Q 260 40 560 50 L560 690 Q 300 850 0 900 Z" fill="var(--card-white)"/>
        <path d="M0 170 Q 260 40 560 50" fill="none" stroke="var(--accent-blue)" stroke-width="6"/>
        <path d="M0 178 Q 260 50 560 60" fill="none" stroke="var(--accent-indigo)" stroke-width="2"/>
        <path d="M560 690 Q 300 850 0 900" fill="none" stroke="var(--accent-blue)" stroke-width="6"/>
        <path d="M560 700 Q 300 860 0 910" fill="none" stroke="var(--accent-indigo)" stroke-width="2"/>
      </svg>

      <header class="brand">
        <span class="brand-dot"></span>
        <p class="brand-name">Moberly Swift<br>Solutions, LLC</p>
      </header>

      <section class="person">
        <h1 class="person-name">Lucia Pembrook</h1>
        <p class="person-title">President</p>
      </section>

      <section class="contact">
        <p class="contact-phone">703-482-1947</p>
        <p class="contact-line">lpembrook@moberlyswiftsolutions.example</p>
        <p class="contact-line">www.moberlyswiftsolutions.example</p>
      </section>
    </article>
  </main>
</body>
</html>
```